Talvane Companies Business Card Design

We need a new business card for our Private Equity Real Estate Development firm, “Talvane” and our EB-5 regional center “Moorfield Regional Center” on one card. We prefer a design that is simple, elegant, and represents the luxury products we design and build as well as the financial security and stability our successful history has produced. We are an industry leader in our field and 3rd generation family business that has evolved into an institutional quality investment platform. Considered design size is standard business card dimensions (3.5 x 2 inches with an additional 1/8 inch space for design elements or backgrounds that extend beyond the finished size of your piece.

Target Market(s)

• High net worth individuals
• Highly skilled technical workers and physicians in the US seeking investment-based immigration opportunities
• Sophisticated private equity investors
• Intermediary partners include domestic attorneys and investment brokers, as well as international agent networks
• US real estate developers

Industry/Entity Type

Finance

Contact Information for Business Card

(Providing placeholder info for personal information, please design for longer character spaces, longer names and addresses etc..)
• Logo for Talvane
• Logo for Moorfield Regional Center
• Full name: Dorian Talvane
• Job title: CEO
• Email address: dtalvane@talvanecompanies.example
• Cell phone number: +1.555.318.4476
• Office number +1.555.240.6185
• Office address: Quillan Court 5, 4817 Vista Ardell, San Ramon, CA.
• Website: www.talvanecompanies.example

Font styles to use
Serif
Sans Serif

Colors
ec1f27
ffffff
000000

Requirements
Must have
• • Logo for Talvane
• • Logo for Moorfield Regional Center
• - Use rounded corners
• (See .ai file included for logos)
Nice to have
• • Simple, elegant design
• • Aesthetically compatible with our website design (www.talvanecompanies.example)
• • Color palette including but not limited to white, black, and red (as per logos)
Should not have
• - Not too much red color
• - Do not stack both logos on top of each other

```html
<!DOCTYPE html>
<html lang="en">
<head>
<meta charset="utf-8">
<title>Talvane Companies – Business Card</title>
<link href="https://fonts.googleapis.com/css2?family=PT+Serif:wght@700&family=Lato:wght@400;700&display=swap" rel="stylesheet">
<style>
  :root {
    --backdrop: #5c5c5c;
    --paper: #ffffff;
    --crimson: #a31a2e;
    --ink: #1a1a1a;
    --night: #050505;
    --slate: #3a3a3a;
    --muted: #555555;
  }
  * { margin: 0; padding: 0; box-sizing: border-box; }
  html, body { width: 1200px; height: 900px; overflow: hidden; }
  body {
    background: var(--backdrop);
    display: flex;
    align-items: center;
    justify-content: center;
    gap: 40px;
    font-family: "Lato", sans-serif;
  }
  .card {
    position: relative;
    width: 540px;
    height: 309px;
    border-radius: 26px;
    overflow: hidden;
  }

  /* Front */
  .card-front { background: var(--paper); }
  .brand-mark {
    position: absolute;
    left: 44px;
    top: 48px;
    display: flex;
    align-items: center;
    gap: 10px;
  }
  .brand-mark .mark-square {
    width: 26px; height: 26px;
    background: var(--crimson);
  }
  .brand-mark .mark-name {
    font-family: "PT Serif", serif;
    font-weight: 700;
    font-size: 20px;
    color: var(--crimson);
    line-height: 1.1;
  }
  .holder {
    position: absolute;
    right: 46px;
    top: 70px;
    text-align: left;
  }
  .holder-name {
    font-family: "PT Serif", serif;
    font-weight: 700;
    font-size: 27px;
    color: var(--crimson);
  }
  .holder-title {
    margin-top: 4px;
    font-size: 15px;
    letter-spacing: 9px;
    color: var(--ink);
  }
  .contact-band {
    position: absolute;
    left: 0; right: 0;
    top: 150px;
    height: 86px;
    background: var(--crimson);
    color: var(--paper);
    display: flex;
    align-items: center;
    padding: 0 30px 0 34px;
    gap: 34px;
    font-size: 13.5px;
  }
  .contact-item { display: flex; align-items: center; gap: 12px; }
  .contact-icon { width: 28px; height: 28px; flex: none; }
  .phone-list { line-height: 1.45; }
  .phone-list .label { display: inline-block; width: 52px; }
  .address {
    position: absolute;
    right: 40px;
    top: 248px;
    font-size: 14px;
    color: var(--ink);
    line-height: 1.45;
    text-align: left;
  }
  .address-line { display: flex; align-items: center; gap: 6px; }
  .pin { width: 11px; height: 14px; }

  /* Back */
  .card-back {
    background: var(--night);
    display: flex;
    flex-direction: column;
    align-items: center;
    justify-content: center;
  }
  .back-brand { display: flex; align-items: center; gap: 16px; }
  .back-brand .mark-square {
    width: 38px; height: 38px;
    background: var(--slate);
  }
  .back-brand .mark-name {
    font-family: "PT Serif", serif;
    font-weight: 700;
    font-size: 46px;
    letter-spacing: 2px;
    color: var(--slate);
  }
  .website {
    margin-top: 26px;
    font-size: 13px;
    color: var(--muted);
    letter-spacing: 0.5px;
  }
</style>
</head>
<body>

  <section class="card card-front">
    <div class="brand-mark">
      <span class="mark-square"></span>
      <span class="mark-name">Moorfield<br>Regional Center</span>
    </div>

    <div class="holder">
      <div class="holder-name">Dorian Talvane</div>
      <div class="holder-title">CEO</div>
    </div>

    <div class="contact-band">
      <div class="contact-item">
        <svg class="contact-icon" viewBox="0 0 28 28" aria-hidden="true">
          <circle cx="14" cy="14" r="14" fill="#fff"/>
          <path d="M10 8c1 0 2 2.5 2 3s-1.2 1-1 1.8c.5 1.6 2.2 3.4 3.8 4 .8.2 1.2-1 1.8-1s3 1 3 2-1.5 2.4-3 2.2C12.5 19.5 8.5 15.5 8 11c-.2-1.5 1-3 2-3z" fill="var(--crimson)"/>
        </svg>
        <div class="phone-list">
          <div><span class="label">Office</span>: +1.555.240.6185</div>
          <div><span class="label">Cell</span>: +1.555.318.4476</div>
        </div>
      </div>
      <div class="contact-item">
        <svg class="contact-icon" viewBox="0 0 28 28" aria-hidden="true">
          <circle cx="14" cy="14" r="14" fill="#fff"/>
          <rect x="7.5" y="9.5" width="13" height="9" fill="none" stroke="var(--crimson)" stroke-width="1.5"/>
          <path d="M7.5 9.5l6.5 5 6.5-5" fill="none" stroke="var(--crimson)" stroke-width="1.5"/>
        </svg>
        <span>dtalvane@talvanecompanies.example</span>
      </div>
    </div>

    <div class="address">
      <div class="address-line">
        <svg class="pin" viewBox="0 0 11 14" aria-hidden="true">
          <path d="M5.5 0A5 5 0 0 0 .5 5c0 3.5 5 9 5 9s5-5.5 5-9a5 5 0 0 0-5-5z" fill="var(--crimson)"/>
          <circle cx="5.5" cy="5" r="1.8" fill="#fff"/>
        </svg>
        <span>Quillan Court 5,</span>
      </div>
      <div>4817 Vista Ardell, San Ramon, CA.</div>
    </div>
  </section>

  <section class="card card-back">
    <div class="back-brand">
      <span class="mark-square"></span>
      <span class="mark-name">TALVANE</span>
    </div>
    <div class="website">www.talvanecompanies.example</div>
  </section>

</body>
</html>
```